Nobody Left the Lantern Burning - Tom Halvery - CD Cover Design Project

Single Cover for CD & Online media e.g. Tunebox Graphics
The first song release from Tom Halvery will be the track 'Nobody Left the Lantern Burning'.
For the release the single requires artwork that is eye catching, seriously professional & meets the requirements of Disc Sprout, Tunebox and also a physical copy on CD.
Track listings for CD will be:
1. Nobody Left the Lantern Burning
2. Nobody Left the Lantern Burning - Instrumental
see details in this link:
http://members.discsprout-example.com/faq.aspx
http://selfmadesound.discsprout-example.com/2009/11/avoid-album-art-atrocities/
http://answers.quorvex-example.com/question/index?qid=20111015141433AAdDTmH
Any advice on this would be greatly appreciated,
I would also like the two logo's I have uploaded to be used,
one is the Tom Halvery logo and the other is for Milbrook & Tandy Records logo (please remove the R and replace with a C for copyright.)
There are four high res photo shopped pictures of Tom Halvery and another zip file of many others, it would be nice to include one of these maybe on the 2nd page or back of the CD. Please don't use them as the front cover.
I imagine an Art Deco illustration but please listen to the track and let it inspire you.
Good Luck
Updates
I don't feel this is what I'm looking for, the design needs to refelct a broken heart without being a picture of a broken heart
Reason: No design has been what we are after so far so the deadline has been extended and the budget increased.

```html
<!DOCTYPE html>
<html lang="en">
<head>
<meta charset="utf-8">
<title>Nobody Left the Lantern Burning – Tom Halvery</title>
<link rel="stylesheet" href="https://fonts.googleapis.com/css2?family=Archivo+Black&family=Open+Sans:wght@400&display=swap">
<style>
  :root {
    --ink: #0d0d0d;
    --paper: #ffffff;
    --surname: #d4d4d4;
    --shadow-grey: #2a2a2a;
    --mid-grey: #6e6e6e;
    --light-grey: #a9a9a9;
  }
  html, body {
    margin: 0;
    padding: 0;
    overflow: hidden;
    background: var(--paper);
  }
  .cover {
    position: relative;
    width: 1200px;
    height: 1200px;
    overflow: hidden;
    background: var(--shadow-grey);
  }
  .cover__artwork {
    position: absolute;
    inset: 0;
    background:
      radial-gradient(ellipse 45% 40% at 58% 38%, var(--light-grey) 0%, var(--mid-grey) 45%, transparent 80%),
      radial-gradient(ellipse 60% 55% at 80% 20%, #8a8a8a 0%, transparent 70%),
      linear-gradient(100deg, #1f1f1f 0%, #3c3c3c 35%, #5a5a5a 60%, #3a3a3a 100%);
  }
  .cover__title {
    position: absolute;
    top: 78px;
    left: 0;
    width: 100%;
    margin: 0;
    text-align: center;
    font-family: "Open Sans", Arial, sans-serif;
    font-weight: 400;
    font-size: 56px;
    letter-spacing: 0.5px;
    color: var(--paper);
    text-transform: uppercase;
  }
  .cover__name {
    position: absolute;
    inset: 0;
    width: 1200px;
    height: 1200px;
  }
  .cover__name text {
    font-family: "Archivo Black", "Arial Black", sans-serif;
  }
  .name-first { fill: var(--ink); fill-opacity: 0.92; }
  .name-last { fill: var(--surname); }
</style>
</head>
<body>
  <main class="cover">
    <div class="cover__artwork" role="img" aria-label="Grainy black and white grunge-textured portrait of the artist filling the cover"></div>
    <h1 class="cover__title">Nobody Left the Lantern Burning</h1>
    <svg class="cover__name" viewBox="0 0 1200 1200" aria-label="Tom Halvery" role="img">
      <text class="name-first" x="0" y="962" font-size="530" textLength="1200" lengthAdjust="spacingAndGlyphs">TOM</text>
      <text class="name-last" x="0" y="1238" font-size="350" textLength="1200" lengthAdjust="spacingAndGlyphs">HALVERY</text>
    </svg>
  </main>
</body>
</html>
```